VERANDOLA - Mother Daughter Piano Duo

My mom and I are performing concert pianists and are arranging (covering) classical piano music for 2 pianists (2 piano songs and also one piano-four hand songs). We need a design for the cover of our single songs and books that we produce. We will be selling our music on our website and will have links to our website store in our ClipHarbor video descriptions. Some of the composers we are arranging music for currently are Kelbrun, Wastel, Gorvk, Menki, Tolvik, Peslin and Vostrelikova. Piano music standard size is 9 x 12 inches. Our spine width will probably be 1/4 inch thick but not more than 1/2 inch.

Target Market(s)

Classical pianists, musicians and teachers

Industry/Entity Type

Clipharbor

Font styles to use
Script

Colors

Designer to choose colors to be used in the design.

Requirements
Must have
• Must have our name “VERANDOLA Mother-Daughter Piano Duo”
Nice to have
• Music symbols or piano designs.

```html
<!DOCTYPE html>
<html lang="en">
<head>
<meta charset="UTF-8">
<title>Verandola – Mother Daughter Piano Duo</title>
<link href="https://fonts.googleapis.com/css2?family=Great+Vibes&family=EB+Garamond:ital,wght@0,600;1,400&display=swap" rel="stylesheet">
<style>
  :root {
    --page-bg: #b3afab;
    --cover-black: #000000;
    --ivory: #f4efe0;
    --key-cream: #e9dcc6;
    --warm-shadow: #3a322a;
  }
  html, body {
    margin: 0;
    width: 1200px;
    height: 800px;
    overflow: hidden;
    background: var(--page-bg);
  }
  .cover {
    position: absolute;
    left: 315px;
    top: 20px;
    width: 570px;
    height: 760px;
    background: var(--cover-black);
    overflow: hidden;
  }
  .cover-title {
    position: absolute;
    left: 36px;
    top: 44px;
    margin: 0;
    font-family: "Great Vibes", cursive;
    font-weight: 400;
    font-size: 108px;
    line-height: 1;
    color: var(--ivory);
  }
  .cover-subtitle {
    position: absolute;
    right: 44px;
    top: 166px;
    margin: 0;
    font-family: "EB Garamond", serif;
    font-style: italic;
    font-size: 24px;
    letter-spacing: 0.5px;
    color: var(--ivory);
  }
  .piano-photo {
    position: absolute;
    left: 0;
    top: 340px;
    width: 570px;
    height: 420px;
    background:
      radial-gradient(ellipse 38% 30% at 42% 30%, rgba(233,220,198,0.85), rgba(233,220,198,0) 100%),
      linear-gradient(160deg, rgba(0,0,0,0) 45%, var(--key-cream) 75%, var(--warm-shadow) 100%),
      linear-gradient(180deg, var(--cover-black) 0%, #1a1612 60%, #2b251e 100%);
  }
  .author-name {
    position: absolute;
    left: 44px;
    top: 692px;
    margin: 0;
    font-family: "EB Garamond", serif;
    font-weight: 600;
    font-size: 31px;
    letter-spacing: 2px;
    color: var(--cover-black);
  }
</style>
</head>
<body>
  <main class="cover">
    <div class="piano-photo" role="img" aria-label="Photograph of a black grand piano keyboard in soft warm light, keys receding diagonally"></div>
    <h1 class="cover-title">Verandola</h1>
    <p class="cover-subtitle">Mother Daughter Piano Duo</p>
    <p class="author-name">Author name</p>
  </main>
</body>
</html>
```